Business Card for a mobile physiotherapy company

I need a layout for a business card for a mobile physiotherapy company.
Slogan is "Mobile Physiotherapy - Your Road To Recovery"
Phone number is 867-402-5913
Email VantrePhysio@mailbright.ca (subject to change with website)
Website www.VantrePhysio.ca
My name and credentials: Kent Vantre Kent Vantre, BSc(kin), MPT, CAFCI, IMS
Information maybe included: Direct Billing, Services including Physiotherapy, IMS, acupuncture
Maybe include facebook and instagram logos
One side with the logo clean and sharp
Other side with details, try not to look too busy, keep everything concise

```html
<!DOCTYPE html>
<html lang="en">
<head>
<meta charset="utf-8">
<title>Vantre Physio – Business Card</title>
<link rel="stylesheet" href="https://fonts.googleapis.com/css2?family=Open+Sans:wght@400;600;700&display=swap">
<style>
  :root {
    --page-bg: #3a3a3c;
    --card-bg: #ffffff;
    --navy: #2c4676;
    --green: #1e5b46;
    --ink: #2a2a2a;
    --rule: #3e6b5a;
  }
  * { box-sizing: border-box; margin: 0; padding: 0; }
  html, body {
    width: 1200px; height: 997px; overflow: hidden;
    background: var(--page-bg);
    font-family: "Open Sans", Arial, sans-serif;
  }
  .sheet {
    position: relative; width: 1200px; height: 997px;
    display: flex; flex-direction: column; align-items: center; justify-content: center; gap: 70px;
  }
  .card {
    position: relative; width: 600px; height: 343px;
    background: var(--card-bg);
    border-radius: 0 56px 0 56px;
    box-shadow: 0 10px 30px rgba(0,0,0,.45);
    overflow: hidden;
  }
  /* logo side */
  .brand-mark {
    position: absolute; left: 0; right: 0; top: 110px;
    display: flex; align-items: center; justify-content: center; gap: 14px;
  }
  .brand-mark__square { width: 18px; height: 18px; background: var(--navy); }
  .brand-mark__name { font-size: 44px; font-weight: 700; color: var(--navy); letter-spacing: 2px; }
  .services {
    position: absolute; left: 0; right: 0; bottom: 46px; text-align: center;
    font-size: 14px; font-weight: 700; color: var(--green);
  }
  /* details side */
  .details .brand-mark { left: 40px; right: auto; top: 140px; justify-content: flex-start; }
  .details .brand-mark__name { font-size: 30px; }
  .divider { position: absolute; left: 318px; top: 70px; width: 1px; height: 140px; background: var(--rule); }
  .person { position: absolute; left: 340px; top: 70px; }
  .person__name { font-size: 15px; font-weight: 700; color: var(--navy); text-transform: uppercase; letter-spacing: .5px; }
  .person__creds { font-size: 11px; color: var(--ink); margin-top: 1px; }
  .contact-list { list-style: none; position: absolute; left: 340px; top: 124px; }
  .contact-list li { display: flex; align-items: center; gap: 8px; font-size: 12.5px; color: var(--ink); line-height: 18px; }
  .contact-list .web { font-weight: 700; }
  .icon { width: 11px; height: 11px; flex: none; fill: #333; }
  .slogan {
    position: absolute; left: 0; right: 0; bottom: 48px; text-align: center;
    font-size: 14px; font-weight: 700; color: var(--green);
  }
</style>
</head>
<body>
<main class="sheet">

  <section class="card logo-side" aria-label="Card front">
    <div class="brand-mark">
      <span class="brand-mark__square"></span>
      <span class="brand-mark__name">Vantre Physio</span>
    </div>
    <p class="services">We offer: Direct Billing,Physiotherapy,IMS,acupuncture</p>
  </section>

  <section class="card details" aria-label="Card back">
    <div class="brand-mark">
      <span class="brand-mark__square"></span>
      <span class="brand-mark__name">Vantre Physio</span>
    </div>
    <div class="divider"></div>
    <div class="person">
      <p class="person__name">Kent Vantre</p>
      <p class="person__creds">BSc(kin), MPT, CAFCI, IMS</p>
    </div>
    <ul class="contact-list">
      <li><svg class="icon" viewBox="0 0 12 12"><path d="M1 3c0-1 1-2 2-2h6c1 0 2 1 2 2v1H8V3H4v1H1z M2 5h8l1 5H1z"/></svg>867-402-5913</li>
      <li><svg class="icon" viewBox="0 0 12 12"><path d="M0 2h12v8H0z" fill="none" stroke="#333" stroke-width="1.4"/><path d="M0 2l6 5 6-5" fill="none" stroke="#333" stroke-width="1.4"/></svg>VantrePhysio@mailbright.ca</li>
      <li><svg class="icon" viewBox="0 0 12 12"><rect x="1" y="1" width="10" height="10"/></svg>VantrePhysio</li>
      <li><svg class="icon" viewBox="0 0 12 12"><rect x="1" y="1" width="10" height="10"/></svg>VantrePhysio.ca</li>
      <li class="web"><svg class="icon" viewBox="0 0 12 12"><circle cx="6" cy="6" r="5" fill="none" stroke="#333" stroke-width="1.4"/><path d="M1 6h10M6 1c-3 3-3 7 0 10M6 1c3 3 3 7 0 10" fill="none" stroke="#333" stroke-width="1"/></svg>www.VantrePhysio.ca</li>
    </ul>
    <p class="slogan">Mobile Physiotherapy - Your Road To Recovery</p>
  </section>

</main>
</body>
</html>
```